Ledgerwise Reach - B2B Demand Generation Website Project

We need a fully functional website for www.ledgerwisereach.example. We are a B2B Demand Generation company, based in London, working with companies such as QRT, VKD, Norvex, Brindlow, Tarvo generating them sales leads for their sales teams. We run this through digital marketing newsletter promotions and have a network of websites. Content syndication, data, demand generation, online marketing. Our logo has just been redone (attached) and we have a holding page already which i would like to use the style / colours. Our logo is bright and vibrant but i dont want the site to be a rainbow. We are expensive, classy, professorial, B2B, intelligent.

Home
About Us
Our Services
Prospora & QA Technology
Intent Data
Testimonials
Contact Us
Updates

Target Market(s)

B2B Marketers (QRT, Velquarion, Tarvo, VKD, Opal Reach, Driftmoor, Harlow Quantis, Technology Companies, Data Companies, Marketing Teams, Tumbleden.

Industry/Entity Type

Marketing

Coding

Coded - Design and coding required

Number of Pages Required

5+ page

Font styles to use
Sans Serif

Requirements
Must have
• Home
About Us
Our Services
Prospora & QA Technology
Intent Data
Testimonials
Contact Us

Simple Pages.

Look classy, intelligent, data experts. I like the video homepages were the image moves at the top. Very soft animation.
Nice to have
• Websites i like:

https://www.vkd.example/
https://www.brevantor.example/
https://www.plumfieldsites.example.co.uk/

Ledgerwise Reach - The Demand Generation Company
Should not have
• Glimpsevault crap images

```html
<!DOCTYPE html>
<html lang="en">
<head>
<meta charset="utf-8">
<title>Ledgerwise Reach - The Demand Generation Company</title>
<link href="https://fonts.googleapis.com/css2?family=Roboto:wght@300;400;500&display=swap" rel="stylesheet">
<style>
:root{
  --navy:#1d4f8f;
  --red:#d3302f;
  --ink:#666a70;
  --soft:#f5f6f8;
  --dark:#3a3a3c;
  --darker:#2b2b2d;
  --white:#fff;
}
*{margin:0;padding:0;box-sizing:border-box}
html,body{width:1200px;height:4435px;overflow:hidden}
body{position:relative;background:var(--white);font-family:'Roboto',sans-serif;color:var(--ink)}
.abs{position:absolute}
.btn-solid{position:absolute;height:40px;border-radius:20px;background:var(--navy);color:#fff;font-size:16px;display:flex;align-items:center;justify-content:center;gap:14px}
.btn-ghost{position:absolute;height:40px;border-radius:20px;border:1.5px solid var(--navy);color:var(--navy);font-size:16px;display:flex;align-items:center;justify-content:center;gap:14px;background:#fff}
.chev{width:8px;height:8px;border-right:1.5px solid currentColor;border-top:1.5px solid currentColor;transform:rotate(45deg)}
.section-title{position:absolute;left:0;width:1200px;text-align:center;color:var(--navy);font-weight:400;font-size:34px}
.section-title span{display:inline-block;position:relative}
.section-title span::after{content:"";position:absolute;left:0;bottom:-10px;width:44px;height:3px;background:var(--red)}
.left-title{position:absolute;color:var(--navy);font-weight:400;font-size:34px}
.left-title::after{content:"";position:absolute;left:0;bottom:-10px;width:44px;height:3px;background:var(--red)}

/* header */
.social-dots{left:86px;top:76px;display:flex;gap:13px}
.social-dots i{width:12px;height:12px;border-radius:50%;background:#8a8d92;display:block}
.brand{left:0;width:1200px;top:22px;display:flex;flex-direction:column;align-items:center}
.brand-mark{width:36px;height:36px;border-radius:50%;border:3px solid var(--red)}
.brand-name{color:var(--red);font-size:20px;margin-top:4px}
.brand-tag{font-size:7px;color:var(--red);margin-top:1px}
.contact-btn{left:964px;top:57px;width:141px;height:42px;border-radius:21px;background:var(--navy);color:#fff;font-size:15px;display:flex;align-items:center;justify-content:center}
.main-nav{top:128px;left:0;width:1200px;font-size:15px;color:#666}
.main-nav a{position:absolute;color:inherit;text-decoration:none}
.main-nav a.active{color:var(--navy)}
.main-nav a.active::after{content:"";position:absolute;left:0;right:0;bottom:-9px;height:2px;background:var(--navy)}

/* hero */
.hero-scene{left:0;top:160px;width:1200px;height:478px;border-radius:0 0 160px 160px;background:radial-gradient(ellipse at 50% 40%,#e4e4e6 0%,#f2f2f3 55%,#fbfbfb 100%);box-shadow:0 10px 30px rgba(0,0,0,.06)}
.hero-copy{left:0;top:206px;width:1200px;display:flex;flex-direction:column;align-items:center}
.quote-mark{color:var(--red);font-size:60px;font-weight:500;line-height:.8;height:38px}
.hero-copy h1{font-weight:300;font-size:31px;color:#555;margin-top:16px}
.hero-copy p{font-weight:300;font-size:20px;color:#777;margin-top:4px}
.dots{display:flex;gap:6px}
.dots i{width:8px;height:8px;border-radius:50%;border:1px solid var(--navy);display:block}
.dots i.on{background:var(--navy)}

/* about */
.about-bg{left:0;top:638px;width:1200px;height:384px;background:var(--soft)}
.about-text{left:170px;width:860px;top:766px;text-align:center;font-size:15px;line-height:26.5px;font-weight:300;color:#555}

/* services */
.card{position:absolute;background:#fff;border-radius:22px;box-shadow:0 4px 26px rgba(30,40,60,.09);width:460px;height:372px}
.card h3{position:absolute;left:52px;top:40px;width:260px;color:var(--navy);font-weight:500;font-size:20px;line-height:26px}
.card p{position:absolute;left:54px;top:118px;width:356px;font-size:14.5px;line-height:19px;text-align:justify;color:#6a6a6a;font-weight:300}
.card .icon{position:absolute;left:48px;top:242px}
.card .btn-solid{left:270px;top:296px;width:142px}
.promo{left:660px;top:1704px;width:380px;text-align:center;color:var(--navy);font-size:20px;line-height:25.5px}
.promo-ring{left:720px;top:1630px;width:260px;height:260px;border-radius:50%;background:radial-gradient(circle,rgba(211,48,47,0) 44%,rgba(211,48,47,.07) 46%,rgba(211,48,47,0) 70%)}

/* qa */
.qa-bg{left:0;top:2023px;width:1200px;height:560px;background:var(--soft)}
.qa-card{left:122px;top:2089px;width:590px;height:382px;border:1.5px solid var(--navy);border-radius:16px;background:#fff}
.qa-text{left:178px;top:2234px;width:368px;font-size:15px;line-height:18.5px;text-align:justify;font-weight:300;color:#555}
.qa-photo{left:573px;top:2183px;width:542px;height:352px;border-radius:18px;background:linear-gradient(160deg,#7d8fb8 0%,#3f5690 55%,#243a72 100%)}
.qa-badge{left:925px;top:2428px;width:158px;height:89px;background:#fff;display:flex;flex-direction:column;align-items:center;justify-content:center;gap:8px}
.qa-badge i{width:18px;height:18px;border-radius:50%;background:#e39a2b;display:block}
.qa-badge span{color:#333;font-size:20px;letter-spacing:2px}

/* stats */
.stats-bg{left:0;top:2630px;width:1200px;height:246px;background:linear-gradient(180deg,#ffffff 0%,#eef2f7 45%,#e1e7ef 100%)}
.stat{position:absolute;width:260px;text-align:center}
.stat b{display:block;color:var(--navy);font-weight:500;font-size:36px}
.stat span{display:block;color:var(--red);font-size:15.5px;line-height:20px;margin-top:14px}

/* intent */
.laptop{left:150px;top:2980px;width:400px;height:270px;border-radius:8px;background:linear-gradient(180deg,#f4f4f5 0%,#dcdde0 50%,#f7f7f8 100%)}
.intent-text{left:653px;top:3046px;width:366px;font-size:15px;line-height:18.7px;text-align:justify;font-weight:300;color:#555}

/* clients */
.clients-bg{left:0;top:3323px;width:1200px;height:430px;background:linear-gradient(180deg,#f5f7fa,#ffffff)}
.avatar{left:538px;top:3427px;width:120px;height:120px;border-radius:50%;background:#d9cfc9}
.quote{left:210px;width:780px;top:3570px;text-align:center;color:var(--red);font-size:14px;line-height:17px;font-weight:300}
.author{left:0;width:1200px;top:3654px;text-align:center;font-size:13px;color:#444;letter-spacing:.5px}

/* partners */
.partner-row{left:170px;top:3848px;width:860px;display:flex;justify-content:space-between;align-items:center;font-size:17px;color:#8a8d92;font-weight:500}
.arrow-l,.arrow-r{top:3846px;width:22px;height:22px;border-left:1.5px solid #999;border-bottom:1.5px solid #999}
.arrow-l{left:92px;transform:rotate(45deg)}
.arrow-r{left:1086px;transform:rotate(-135deg)}

/* footer */
.footer{left:0;top:3938px;width:1200px;height:416px;background:var(--dark);color:#fff}
.footer-base{left:0;top:4353px;width:1200px;height:82px;background:var(--darker);color:#ddd;font-size:13px;display:flex;align-items:center;justify-content:center}
.f-brand{left:107px;top:3995px;width:206px;display:flex;flex-direction:column;align-items:center;color:#fff}
.f-brand i{width:52px;height:52px;border-radius:50%;border:3px solid #fff;display:block}
.f-brand b{font-weight:300;font-size:26px;margin-top:6px;white-space:nowrap}
.f-brand small{font-size:8px;margin-top:2px}
.f-about{left:105px;top:4128px;width:250px;font-size:10px;line-height:15px;text-align:justify;color:#eee}
.f-social{left:105px;top:4222px;display:flex;gap:12px}
.f-social i{width:24px;height:24px;border-radius:50%;border:2px solid #fff;display:block}
.f-col{position:absolute;font-size:15px;color:#eee}
.f-col h4{font-weight:400;font-size:15px;margin-bottom:26px}
.f-col li{list-style:none;height:36px;white-space:nowrap}
</style>
</head>
<body>

<header>
  <div class="abs social-dots" aria-label="Social links"><i></i><i></i><i></i><i></i></div>
  <div class="abs brand">
    <div class="brand-mark"></div>
    <div class="brand-name">Ledgerwise Reach</div>
    <div class="brand-tag">The Demand Generation Company</div>
  </div>
  <a class="abs contact-btn">CONTACT US</a>
</header>

<section class="hero">
  <div class="abs hero-scene" role="img" aria-label="Bright studio desk scene with a desktop computer, desk lamp, pencil pot, teapot and plant"></div>
  <div class="abs hero-copy">
    <div class="quote-mark">&ldquo;</div>
    <h1>Ledgerwise Reach Offers</h1>
    <p>multi-channel demandgeneration services</p>
    <a class="btn-ghost" style="position:relative;margin-top:30px;width:130px;height:34px;font-size:15px">Get Started <i class="chev"></i></a>
  </div>
  <div class="abs dots" style="left:580px;top:580px"><i></i><i class="on"></i><i></i></div>
</section>

<nav class="abs main-nav">
  <a class="active" style="left:305px">HOME</a>
  <a style="left:396px">ABOUT</a>
  <a style="left:491px">SERVICES</a>
  <a style="left:613px">QA TECHNOLOGY</a>
  <a style="left:790px">INTEND DATA</a>
</nav>

<section class="about">
  <div class="abs about-bg"></div>
  <h2 class="section-title" style="top:692px"><span>About Us</span></h2>
  <p class="abs about-text">Ledgerwise Reach can deliver high quality sales leads from any country in the world. This can include leads via email or tele-marketing, account-based targeting (ABM) or identifying need and pain points through BANT / SQL campaigns. Ledgerwise Reach offer expert demand generation support, from providing detailed leads of qualified decision-makers, to a comprehensive lead generation and SQL service.</p>
  <a class="btn-solid" style="left:529px;top:922px;width:142px">Read More <i class="chev"></i></a>
</section>

<section class="services">
  <h2 class="section-title" style="top:1052px"><span>Our Services</span></h2>

  <article class="card" style="left:124px;top:1173px">
    <h3>Marketing Qualified Leads (MQL)</h3>
    <p>A Marketing Qualified Lead (MQL) is a prospect that has expressed an interest in what your brand has to offer. An MQL has taken the first steps to becoming a customer and is ready to receive additional contact from your company. From a very general perspective</p>
    <svg class="icon" width="112" height="120" viewBox="0 0 112 120"><path d="M56 4a50 50 0 1 0 20 96l14 14-2-20A50 50 0 0 0 56 4z" fill="none" stroke="#d3302f" stroke-width="2"/><g fill="none" stroke="#d3302f" stroke-width="2"><rect x="40" y="28" width="32" height="14" rx="7"/><circle cx="38" cy="58" r="6"/><circle cx="56" cy="58" r="6"/><circle cx="74" cy="58" r="6"/><path d="M28 78c0-8 20-8 20 0M46 78c0-8 20-8 20 0M64 78c0-8 20-8 20 0"/></g></svg>
    <a class="btn-solid">Read More <i class="chev"></i></a>
  </article>

  <article class="card" style="left:616px;top:1173px">
    <h3>Account Based Marketing Leads (ABM)</h3>
    <p>A Marketing Qualified Lead (MQL) is a prospect that has expressed an interest in what your brand has to offer. An MQL has taken the first steps to becoming a customer and is ready to receive additional contact from your company. From a very general perspective</p>
    <svg class="icon" width="112" height="120" viewBox="0 0 112 120"><path d="M56 4a50 50 0 1 0 20 96l14 14-2-20A50 50 0 0 0 56 4z" fill="none" stroke="#d3302f" stroke-width="2"/><g fill="none" stroke="#d3302f" stroke-width="2"><circle cx="56" cy="48" r="8"/><path d="M44 70c0-12 24-12 24 0"/><circle cx="32" cy="36" r="5"/><circle cx="80" cy="36" r="5"/><circle cx="32" cy="70" r="5"/><circle cx="80" cy="70" r="5"/></g></svg>
    <a class="btn-solid">Read More <i class="chev"></i></a>
  </article>

  <article class="card" style="left:127px;top:1581px">
    <h3>Sales Qualified Lead / BANT</h3>
    <p>A Marketing Qualified Lead (MQL) is a prospect that has expressed an interest in what your brand has to offer. An MQL has taken the first steps to becoming a customer and is ready to receive additional contact from your company. From a very general perspective</p>
    <svg class="icon" width="112" height="120" viewBox="0 0 112 120"><path d="M56 4a50 50 0 1 0 20 96l14 14-2-20A50 50 0 0 0 56 4z" fill="none" stroke="#d3302f" stroke-width="2"/><g fill="none" stroke="#d3302f" stroke-width="2"><rect x="34" y="26" width="44" height="26" rx="3"/><circle cx="40" cy="62" r="5"/><circle cx="56" cy="62" r="5"/><circle cx="72" cy="62" r="5"/><path d="M30 80c0-8 20-8 20 0M46 80c0-8 20-8 20 0M62 80c0-8 20-8 20 0"/></g></svg>
    <a class="btn-solid">Read More <i class="chev"></i></a>
  </article>

  <div class="abs promo-ring"></div>
  <p class="abs promo">We are a prospect that has expressed an interest in what your brand has to offer. An MQL has taken the first steps to be Leads</p>
  <a class="btn-ghost" style="left:790px;top:1822px;width:118px;height:34px;font-size:15px">Explore <i class="chev"></i></a>
</section>

<section class="qa">
  <div class="abs qa-bg"></div>
  <div class="abs qa-card"></div>
  <h2 class="left-title" style="left:178px;top:2150px">QA Technologies</h2>
  <p class="abs qa-text">Prospora is a proprietary lead verification platform from Ledgerwise Reach that aims to sift out invalid leads with questionable or erroneous data. The platform is designed to equip sales teams with accurate, high-quality records in order to improve lead generation, accelerate pipeline and increase revenue.</p>
  <a class="btn-ghost" style="left:176px;top:2377px;width:142px">Explore <i class="chev"></i></a>
  <div class="abs qa-photo" role="img" aria-label="Blue-toned night city skyline with glowing network arcs connecting buildings"></div>
  <div class="abs qa-badge"><i></i><span>PROSPORA</span></div>
</section>

<section class="stats">
  <div class="abs stats-bg" role="img" aria-label="Faint pale blue city skyline behind the figures"></div>
  <div class="stat" style="left:161px;top:2706px"><b>70,000+</b><span>Downloads<br>Per Month</span></div>
  <div class="stat" style="left:471px;top:2706px"><b>25,000+</b><span>Leads Delivered<br>Per Month</span></div>
  <div class="stat" style="left:779px;top:2706px"><b>50+</b><span>Countries<br>We Can Reach</span></div>
</section>

<section class="intent">
  <div class="abs laptop" role="img" aria-label="Open laptop showing a grid of colourful app tiles"></div>
  <h2 class="left-title" style="left:653px;top:2954px">Intent Data</h2>
  <p class="abs intent-text">Our relationships with the world's most important technology &amp; business decisions-makers generate a perpetual stream of global data. With access to 35 million individuals and a global behavioural data stream that is authenticated, timely and contextually relevant, we have one of</p>
  <a class="btn-ghost" style="left:653px;top:3185px;width:142px">Explore <i class="chev"></i></a>
</section>

<section class="clients">
  <div class="abs clients-bg"></div>
  <h2 class="section-title" style="top:3350px"><span>Clients Say</span></h2>
  <div class="abs avatar" role="img" aria-label="Portrait photo of the client giving the testimonial"></div>
  <p class="abs quote">Neque porro quisquam est qui dolorem ipsum quia dolor sit amet, consectetur, adipisci velit There is no one who loves pain itself, who seeks after it and wants to have it, simply because it is pain neque porro quisquam est qui dolorem ipsum quia dolor sit amet, consectetur, adi who seeks after it and wants to have it, simply because it is pain.</p>
  <p class="abs author">- MARA ELLISON</p>
  <div class="abs dots" style="left:580px;top:3696px"><i></i><i class="on"></i><i></i></div>
</section>

<section class="partners">
  <div class="abs arrow-l"></div>
  <div class="abs partner-row">
    <span>QRT</span><span>Calverin</span><span>VKD</span><span>Tarvo</span><span>Orlentis</span><span>Pellaroc</span><span>Dunmere</span><span>Skyvanta</span><span>Ostrelle</span>
  </div>
  <div class="abs arrow-r"></div>
</section>

<footer>
  <div class="abs footer"></div>
  <div class="abs f-brand"><i></i><b>ledgerwise reach</b><small>The Demand Generation Company</small></div>
  <p class="abs f-about">Ledgerwise Reach can deliver high quality sales leads from any country in the world. This can include leads via email or telemarketing, account-based targeting (ABM) or identifying need and pain points through</p>
  <div class="abs f-social"><i></i><i></i><i></i><i></i></div>
  <div class="f-col" style="left:439px;top:4044px"><h4>MENUS</h4><ul><li>Home</li><li>About Us</li><li>Services</li><li>QA Technology</li><li>Intend Data</li></ul></div>
  <div class="f-col" style="left:625px;top:4044px"><h4>QUICK LINKS</h4><ul><li>Services</li><li>Copy Right</li><li>Terms &amp; condition</li><li>Privacy Policy</li></ul></div>
  <div class="f-col" style="left:870px;top:4044px;font-size:14px"><h4>CONTACT US</h4><ul><li>Phone:&nbsp; 020-7946-0000</li><li>email: sales@ledgerwisereach.example</li><li>Address: Lorem plase, area street,</li><li>place area.</li></ul></div>
  <div class="abs footer-base">© 2020 ledgerwise reach. All rights reserved.</div>
</footer>

</body>
</html>
```